Business Card design for Accounting and Consulting Firm
R.T. BALLISTER HOLDINGS, LLC
Business Card design for Accounting and Consulting Firm - Financial Services
Creative Brief
Use same font as used in my logo
trajan bold
Professional
Nell Whitcombe
President
I do not want address on the card
nwhitcombe@rtballister-example.com
www.rtballister-example.com
CFO Advisory / Bookkeeping Plinwor Ledgerly Consulting
either logo without text or logo with text whichever is not used on the front of card.
rtballister rtballister
You can use other fonts, I just listed the one that is used in the text with the logo so you would know what that is. Pantone Hex Colors used: BLUE #012377 (C:96 - M:77 - Y:14 - K:4) #021856 (C:96 - M:82 - Y:28 - K:16) #095CD3 (C:95 - M:47 - Y:0 - K:0) Gold #987412 (C:29 - M:37 - Y:91 - K:16) #E4BB2C (C:9 - M:23 - Y:82 - K:1)

```html
<!DOCTYPE html>
<html lang="en">
<head>
<meta charset="utf-8">
<title>R.T. Ballister Holdings, LLC — Business Cards</title>
<link href="https://fonts.googleapis.com/css2?family=Cinzel:wght@400;700&family=Cormorant+Garamond:wght@500;600&display=swap" rel="stylesheet">
<style>
  :root {
    --blue: #012377;
    --blue-deep: #021856;
    --blue-bright: #095CD3;
    --gold: #987412;
    --gold-light: #E4BB2C;
    --white: #ffffff;
    --ink: #1d2b5c;
    --grey: #555a66;
    --backdrop: #eceae6;
  }
  * { box-sizing: border-box; margin: 0; padding: 0; }
  html, body { width: 1200px; height: 799px; overflow: hidden; }
  body { background: var(--backdrop); position: relative; }

  .card {
    position: absolute;
    width: 540px; height: 310px;
    border-radius: 22px;
    overflow: hidden;
    box-shadow: 0 6px 22px rgba(0,0,0,0.18);
    background: var(--white);
  }
  .card-front { left: 40px; top: 245px; }
  .card-back { left: 620px; top: 245px; }
  .card svg.card-art { position: absolute; inset: 0; width: 100%; height: 100%; }

  /* Front */
  .brand { position: absolute; left: 30px; top: 188px; display: flex; align-items: center; gap: 14px; }
  .brand-dot { width: 48px; height: 48px; border-radius: 50%; background: var(--blue); }
  .brand-name {
    font-family: 'Cinzel', serif; font-weight: 700; color: var(--blue);
    font-size: 27px; line-height: 1.05; letter-spacing: 0.5px;
  }
  .brand-name .brand-sub { display: block; font-size: 16px; letter-spacing: 1.5px; text-align: right; }
  .services {
    position: absolute; left: 30px; top: 274px; display: flex; gap: 22px;
    font-family: 'Cormorant Garamond', serif; font-weight: 600; font-size: 12px; color: var(--blue);
  }
  .service { display: flex; align-items: center; gap: 5px; }
  .service svg { width: 10px; height: 10px; }

  /* Back */
  .person { position: absolute; left: 0; top: 30px; width: 300px; text-align: center; }
  .person-name { font-family: 'Cinzel', serif; font-weight: 700; font-size: 28px; color: var(--blue); letter-spacing: 0.5px; }
  .person-title { font-family: 'Cinzel', serif; font-weight: 700; font-size: 18px; color: var(--gold); letter-spacing: 1px; margin-top: 2px; }
  .contacts { position: absolute; left: 30px; top: 118px; list-style: none; }
  .contacts li {
    display: flex; align-items: center; gap: 8px; height: 24px;
    font-family: 'Cormorant Garamond', serif; font-weight: 600; font-size: 14px; color: var(--grey);
  }
  .contacts .icon {
    width: 15px; height: 15px; border-radius: 50%; background: var(--gold-light);
    display: flex; align-items: center; justify-content: center;
  }
  .contacts .icon svg { width: 9px; height: 9px; }
  .contacts .email { text-transform: uppercase; font-size: 11.5px; }
  .contacts .web { text-transform: uppercase; font-size: 12px; }
</style>
</head>
<body>

<section class="card card-front" aria-label="Business card front">
  <svg class="card-art" viewBox="0 0 540 310" preserveAspectRatio="none" aria-hidden="true">
    <defs>
      <linearGradient id="frontBlue" x1="0" y1="0" x2="1" y2="1">
        <stop offset="0" stop-color="#095CD3"/>
        <stop offset="0.55" stop-color="#012377"/>
        <stop offset="1" stop-color="#021856"/>
      </linearGradient>
      <linearGradient id="frontGold" x1="0" y1="0" x2="1" y2="0">
        <stop offset="0" stop-color="#987412"/>
        <stop offset="0.5" stop-color="#E4BB2C"/>
        <stop offset="1" stop-color="#987412"/>
      </linearGradient>
    </defs>
    <rect width="540" height="310" fill="url(#frontBlue)"/>
    <ellipse cx="345" cy="335" rx="440" ry="228" fill="url(#frontGold)"/>
    <ellipse cx="362" cy="350" rx="440" ry="226" fill="#ffffff"/>
  </svg>
  <div class="brand">
    <span class="brand-dot"></span>
    <div class="brand-name">R.T. BALLISTER<span class="brand-sub">HOLDINGS, LLC</span></div>
  </div>
  <div class="services">
    <span class="service"><svg viewBox="0 0 10 10"><path d="M1 5.5 L4 8.5 L9 1.5" fill="none" stroke="#E4BB2C" stroke-width="1.8"/></svg>CFO Advisory</span>
    <span class="service"><svg viewBox="0 0 10 10"><path d="M1 5.5 L4 8.5 L9 1.5" fill="none" stroke="#E4BB2C" stroke-width="1.8"/></svg>Bookkeeping</span>
    <span class="service"><svg viewBox="0 0 10 10"><path d="M1 5.5 L4 8.5 L9 1.5" fill="none" stroke="#E4BB2C" stroke-width="1.8"/></svg>Plinwor Ledgerly Consulting</span>
  </div>
</section>

<section class="card card-back" aria-label="Business card back">
  <svg class="card-art" viewBox="0 0 540 310" preserveAspectRatio="none" aria-hidden="true">
    <defs>
      <linearGradient id="backBlue" x1="0" y1="0" x2="1" y2="1">
        <stop offset="0" stop-color="#095CD3"/>
        <stop offset="0.5" stop-color="#012377"/>
        <stop offset="1" stop-color="#021856"/>
      </linearGradient>
      <linearGradient id="backGold" x1="0" y1="0" x2="0" y2="1">
        <stop offset="0" stop-color="#987412"/>
        <stop offset="0.5" stop-color="#E4BB2C"/>
        <stop offset="1" stop-color="#987412"/>
      </linearGradient>
    </defs>
    <rect width="540" height="310" fill="url(#backBlue)"/>
    <ellipse cx="180" cy="150" rx="318" ry="262" fill="url(#backGold)"/>
    <ellipse cx="162" cy="150" rx="312" ry="258" fill="#ffffff"/>
  </svg>
  <div class="person">
    <div class="person-name">NELL WHITCOMBE</div>
    <div class="person-title">PRESIDENT</div>
  </div>
  <ul class="contacts">
    <li><span class="icon"><svg viewBox="0 0 10 10"><path d="M2 1 L4 1 L4.6 3 L3.5 4 Q4.5 6 6 6.5 L7 5.4 L9 6 L9 8 Q5 9 1 3 Z" fill="#fff"/></svg></span>555.014.2217</li>
    <li><span class="icon"><svg viewBox="0 0 10 10"><rect x="3" y="1" width="4" height="8" rx="0.8" fill="#fff"/></svg></span>555.018.6403</li>
    <li><span class="icon"><svg viewBox="0 0 10 10"><rect x="1.5" y="3" width="7" height="5" fill="#fff"/><rect x="3" y="1" width="4" height="2.5" fill="#fff"/></svg></span>555.027.9150</li>
    <li class="email"><span class="icon"><svg viewBox="0 0 10 10"><rect x="1" y="2.5" width="8" height="5" fill="#fff"/><path d="M1 2.5 L5 5.5 L9 2.5" fill="none" stroke="#E4BB2C" stroke-width="0.8"/></svg></span>nwhitcombe@rtballister-example.com</li>
    <li class="web"><span class="icon"><svg viewBox="0 0 10 10"><circle cx="5" cy="5" r="3.6" fill="none" stroke="#fff" stroke-width="1"/><path d="M1.4 5 H8.6 M5 1.4 V8.6" stroke="#fff" stroke-width="0.8"/></svg></span>www.rtballister-example.com</li>
  </ul>
</section>

</body>
</html>
```